Bright Path Therapies business cards and stationary

Need business cards and stationary designed to match previously made logo for for a new company based in Sydney NSW called 'Bright Path Therapies'.

We provide early intervention services and diagnostic assessment for children with disability and their families. I would like designs that are colourful and child friendly - possibly using feet/footprints/steps on a white background. The final design should communicate that we are family friendly, accepting and fun to work with.

Target Market(s)

Parents and Families
Teachers
Allied Health Professionals

Industry/Entity Type

Psychology

Contact Information for Business Card

Bright Path Therapies
www.brightpaththerapies.example
info@brightpaththerapies.example

Font styles to use
Sans Serif
Decorative
Script

Requirements
Must have
• Match the font and colour scheme of logo, along with footprint picture
Nice to have
• Clean and simple, while reflecting that I am working with families.
• Also- editable for when we make staff specific cards.

```html
<!DOCTYPE html>
<html lang="en">
<head>
<meta charset="utf-8">
<title>Bright Path Therapies – Business Card</title>
<link href="https://fonts.googleapis.com/css2?family=Rubik:wght@400&family=Lobster&display=swap" rel="stylesheet">
<style>
  :root {
    --backdrop: #1c1c1c;
    --card-white: #ffffff;
    --card-dark: #3a3a3a;
    --brand-red: #ee4c45;
    --brand-blue: #3179c1;
    --brand-orange: #f5a130;
    --brand-green: #79b83a;
    --ink: #2b2b2b;
  }
  * { margin: 0; padding: 0; box-sizing: border-box; }
  html, body { width: 1200px; height: 1200px; overflow: hidden; }
  body {
    background: var(--backdrop);
    font-family: "Rubik", Arial, sans-serif;
    position: relative;
  }
  .card {
    position: absolute;
    left: 194px;
    width: 812px;
    height: 454px;
    border-radius: 20px;
    overflow: hidden;
  }
  .card--front { top: 106px; background: var(--card-white); }
  .card--back { top: 642px; background: var(--card-dark); }

  .brand {
    position: absolute;
    display: flex;
    align-items: center;
    gap: 14px;
  }
  .brand__dot {
    border-radius: 50%;
    background: var(--brand-red);
    flex: none;
  }
  .brand__name {
    color: var(--brand-blue);
    font-weight: 400;
    white-space: nowrap;
  }
  .card--front .brand { left: 22px; top: 42px; }
  .card--front .brand__dot { width: 62px; height: 62px; }
  .card--front .brand__name { font-size: 34px; }

  .card--back .brand {
    left: 50%; top: 50%;
    transform: translate(-50%, -50%);
    gap: 22px;
  }
  .card--back .brand__dot { width: 110px; height: 110px; }
  .card--back .brand__name { font-size: 52px; }

  .tagline {
    position: absolute;
    left: 25px;
    top: 206px;
    font-family: "Lobster", cursive;
    font-size: 37px;
    letter-spacing: -0.5px;
    white-space: nowrap;
  }
  .tagline .w1 { color: var(--brand-orange); }
  .tagline .w2 { color: var(--brand-green); }
  .tagline .w3 { color: var(--brand-blue); }

  .contact {
    position: absolute;
    left: 25px;
    top: 276px;
    list-style: none;
    color: var(--ink);
  }
  .contact__item {
    display: flex;
    align-items: center;
    gap: 7px;
    white-space: nowrap;
  }
  .contact__item svg { flex: none; }
  .contact__item--phone { font-size: 22px; height: 30px; }
  .contact__item--email { font-size: 19px; height: 30px; margin-top: 8px; }
  .contact__item--web { font-size: 19px; height: 30px; margin-top: 6px; }

  .footer-bands { position: absolute; left: 0; bottom: 0; }
  .footer-url {
    position: absolute;
    right: 15px;
    bottom: 16px;
    color: #ffffff;
    font-size: 17px;
    letter-spacing: 0.3px;
  }
</style>
</head>
<body>

<section class="card card--front" aria-label="Business card front">
  <div class="brand">
    <span class="brand__dot"></span>
    <span class="brand__name">Bright Path Therapies</span>
  </div>

  <h1 class="tagline"><span class="w1">Bright</span> <span class="w2">Path</span> <span class="w3">Therapies</span></h1>

  <ul class="contact">
    <li class="contact__item contact__item--phone">
      <svg width="24" height="24" viewBox="0 0 24 24" aria-hidden="true">
        <rect width="24" height="24" rx="4" fill="var(--brand-red)"/>
        <path d="M8 5c-1 0-2.5 1.2-2.5 2.6 0 5 5.8 10.9 10.9 10.9 1.4 0 2.6-1.5 2.6-2.5l-2.6-2.2-1.8 1.3c-2-.9-4.1-3-5-5l1.3-1.8z" fill="#fff"/>
      </svg>
      555-010-2468
    </li>
    <li class="contact__item contact__item--email">
      <svg width="28" height="20" viewBox="0 0 28 20" aria-hidden="true">
        <rect width="28" height="20" rx="2" fill="var(--brand-red)"/>
        <path d="M1.5 2l12.5 9 12.5-9" fill="none" stroke="#fff" stroke-width="2"/>
      </svg>
      info@brightpaththerapies.example
    </li>
    <li class="contact__item contact__item--web">
      <svg width="22" height="22" viewBox="0 0 22 22" aria-hidden="true">
        <circle cx="11" cy="11" r="11" fill="var(--brand-red)"/>
        <path d="M6 5c2 1 3 0 4 2s-1 3 1 4 3 2 2 5M14 3c0 2 2 3 4 3" fill="none" stroke="#fff" stroke-width="1.8"/>
      </svg>
      www.brightpaththerapies.example
    </li>
  </ul>

  <svg class="footer-bands" width="812" height="50" viewBox="0 0 812 50" aria-hidden="true">
    <polygon points="0,6 492,6 486,16 0,16" fill="var(--brand-red)"/>
    <polygon points="0,23 812,23 812,50 0,50" fill="var(--brand-blue)"/>
    <polygon points="508,0 812,0 812,50 490,50" fill="var(--brand-blue)"/>
  </svg>
  <span class="footer-url">www.brightpaththerapies.example</span>
</section>

<section class="card card--back" aria-label="Business card back">
  <div class="brand">
    <span class="brand__dot"></span>
    <span class="brand__name">Bright Path Therapies</span>
  </div>
</section>

</body>
</html>
```